Natural deodorant label

Natural clean deodorant line. Need modernize label which can be sized for both the regular and travel size deodorants. 2.75 x 3" and 1x2". Important to highlight no baking soda and its natural. Also has no aluminum, preservatives, nor chemicals. Its gender inclusive and safe for all ages. Please see website at www.lorvatique.com. will attach current label. Will need a label that i would be able to update with new scents as they come. Want a clean look.
Updates

Need extra days to review

Target Market(s)

the working mother/wife that lives a clean healthy life and pushes that for her family

Industry/Entity Type

health and beauty/deodorant/natural

Colors

Designer to choose colors to be used in the design.

Requirements
Must have
• No baking soda and gender inclusive on label. Clean look. Very little to no picture art.
Nice to have
• Potentially a different color representing the different scents. A brief description of the deodorant scent underneath the scent name. This can be found under the drop down menu titled valdora deodorant scents on the website www.lorvatique.com. Area on front label for a small barcode.
Should not have
• misspelled words; dark label

```html
<!DOCTYPE html>
<html lang="en">
<head>
<meta charset="utf-8">
<title>Lorvatique Valdora Deodorant Label</title>
<link href="https://fonts.googleapis.com/css2?family=Cinzel:wght@600&family=Allura&family=Alegreya+SC:wght@700&family=Alegreya:wght@700&family=Roboto:wght@400;500;700&display=swap" rel="stylesheet">
<style>
  :root {
    --rust: #8a2c17;
    --rust-line: #b9553f;
    --cream: #fdf8f7;
    --ink: #141414;
    --grey: #3b3d42;
    --backdrop: #efefef;
    --blush: #f6e3dc;
  }
  * { box-sizing: border-box; margin: 0; padding: 0; }
  html, body { width: 1200px; height: 1200px; overflow: hidden; background: var(--backdrop); }
  .canvas { position: relative; width: 1200px; height: 1200px; }

  .label {
    position: absolute; top: 128px; width: 472px; height: 943px;
    background: var(--cream);
    box-shadow: -12px 8px 10px rgba(0,0,0,.5);
    overflow: hidden;
  }
  .label--front { left: 93px; }
  .label--back { left: 635px; }
  .band-top { position: absolute; left: 0; top: 0; width: 100%; height: 32px; background: var(--rust); }

  .brand-mark { position: absolute; left: 50%; transform: translateX(-50%); border: 6px solid var(--ink); border-radius: 50%; }
  .brand-name {
    position: absolute; left: 0; width: 100%; text-align: center;
    font-family: 'Cinzel', serif; font-weight: 600; color: var(--ink); letter-spacing: 1px;
  }

  /* front */
  .label--front .brand-mark { top: 78px; width: 130px; height: 130px; }
  .label--front .brand-name { top: 228px; font-size: 58px; letter-spacing: 1.5px; }
  .scent-line {
    position: absolute; left: 0; top: 440px; width: 100%; text-align: center;
    font-family: 'Allura', cursive; font-size: 150px; line-height: 1; color: var(--rust);
  }
  .claims { position: absolute; top: 595px; left: 0; width: 100%; display: flex; justify-content: center; align-items: center; gap: 18px; }
  .claim { display: flex; align-items: center; gap: 10px; font-family: 'Roboto', sans-serif; font-weight: 500; font-size: 19px; line-height: 22px; color: var(--grey); }
  .claim svg { flex: none; }
  .claims .divider { width: 3px; height: 50px; background: var(--grey); }
  .scent-name {
    position: absolute; top: 670px; width: 100%; text-align: center;
    font-family: 'Alegreya SC', serif; font-weight: 700; font-size: 40px; color: var(--rust); letter-spacing: 1px;
  }
  .rule { position: absolute; left: 0; top: 739px; width: 100%; height: 3px; background: var(--rust); }
  .footer-band { position: absolute; left: 0; top: 749px; width: 100%; height: 194px; background: var(--rust); text-align: center; color: var(--blush); }
  .tagline { font-family: 'Allura', cursive; font-size: 54px; line-height: 1; padding-top: 32px; white-space: nowrap; }
  .footer-band .site { font-family: 'Alegreya', serif; font-weight: 700; font-size: 20px; letter-spacing: 3.5px; margin-top: 16px; }
  .net-wt { font-family: 'Roboto', sans-serif; font-size: 14px; margin-top: 14px; opacity: .9; }

  /* back */
  .band-bottom { position: absolute; left: 0; bottom: 0; width: 100%; height: 31px; background: var(--rust); }
  .info-frame { position: absolute; left: 30px; top: 194px; width: 412px; height: 569px; border: 1.5px solid var(--rust-line); }
  .info-frame .brand-mark { top: 24px; width: 84px; height: 84px; border-width: 5px; }
  .info-frame .brand-name { top: 116px; font-size: 37px; }
  .features { position: absolute; left: 50px; top: 208px; list-style: none; }
  .features li { display: flex; align-items: center; gap: 12px; height: 39px; font-family: 'Alegreya', serif; font-weight: 700; font-size: 25px; color: var(--rust); }
  .ingredients { position: absolute; left: 20px; right: 20px; top: 348px; text-align: center; font-family: 'Roboto', sans-serif; font-size: 17px; line-height: 22px; color: var(--grey); }
  .ethics { position: absolute; top: 478px; width: 100%; text-align: center; font-family: 'Roboto', sans-serif; font-weight: 700; font-size: 24px; color: var(--grey); }
  .info-frame .site { position: absolute; top: 524px; width: 100%; text-align: center; font-family: 'Alegreya', serif; font-weight: 700; font-size: 24px; letter-spacing: 3px; color: var(--rust); }
</style>
</head>
<body>
<main class="canvas">

  <section class="label label--front">
    <div class="band-top"></div>
    <div class="brand-mark"></div>
    <div class="brand-name">LORVATIQUE</div>
    <div class="scent-line">Valdora</div>
    <div class="claims">
      <div class="claim">
        <svg width="34" height="34" viewBox="0 0 34 34" fill="none" stroke="#3b3d42" stroke-width="2"><circle cx="17" cy="17" r="15"/><rect x="10" y="10" width="14" height="14"/><line x1="7" y1="7" x2="27" y2="27"/></svg>
        <span>NO BAKING<br>SODA</span>
      </div>
      <div class="divider"></div>
      <div class="claim">
        <svg width="34" height="40" viewBox="0 0 34 40" fill="none" stroke="#3b3d42" stroke-width="2"><circle cx="9" cy="6" r="3.5"/><circle cx="25" cy="6" r="3.5"/><path d="M4 13h10v14H4z"/><path d="M25 12l-6 16h12z"/><line x1="17" y1="4" x2="17" y2="38"/></svg>
        <span>UNISEX<br>DEODORANT</span>
      </div>
    </div>
    <div class="scent-name">TRANQUILITY</div>
    <div class="rule"></div>
    <div class="footer-band">
      <div class="tagline">Naturally Refreshing</div>
      <div class="site">WWW.LORVATIQUE.COM</div>
      <div class="net-wt">NET WT 2.5 OZ (70G)</div>
    </div>
  </section>

  <section class="label label--back">
    <div class="band-top"></div>
    <div class="info-frame">
      <div class="brand-mark"></div>
      <div class="brand-name">LORVATIQUE</div>
      <ul class="features">
        <li><svg width="28" height="28" viewBox="0 0 28 28" fill="none" stroke="#3b3d42" stroke-width="2"><circle cx="14" cy="14" r="12" stroke-dasharray="3 2"/><path d="M14 21V9M14 14l-4-3M14 12l4-3"/></svg>100% ORGANIC</li>
        <li><svg width="28" height="28" viewBox="0 0 28 28" fill="none" stroke="#3b3d42" stroke-width="2"><circle cx="14" cy="14" r="12"/><circle cx="14" cy="11" r="3"/><path d="M8 19h12"/></svg>ALUMINUM FREE</li>
        <li><svg width="28" height="28" viewBox="0 0 28 28" fill="none" stroke="#3b3d42" stroke-width="2"><circle cx="14" cy="14" r="12"/><path d="M9 9v10M19 9v10M14 7v14"/></svg>UNISEX DEODORANT</li>
      </ul>
      <p class="ingredients">Ingredients: Raw alkaline coconut oil,<br>Mango butter, arrowroot powder,<br>candelilla wax, zinc ricinoleate, zinc<br>powder, Vitamin E oil, fragrance</p>
      <div class="ethics">CRUELTY FREE VEGAN</div>
      <div class="site">WWW.LORVATIQUE.COM</div>
    </div>
    <div class="band-bottom"></div>
  </section>

</main>
</body>
</html>
```